Italian restaurant needs new site

Need to make our website better.

Must have reservation module

Must be able to sell wine tasting tours and wine pairing tours and intégrate with tolvo desk

Blog

Social media

Wandermeter ranking and last review.

Number of Pages Required

1 page

Font styles to use
Serif

Requirements
Must have
• Reservation module
• Marketplace to buy wine pairings and gift certificates
• Wandermeter review
• Chatterly posts
• All info from old site

```html
<!DOCTYPE html>
<html lang="en">
<head>
<meta charset="utf-8">
<title>Vinora Bistro – Italian Cuisine &amp; Wine Bar</title>
<link href="https://fonts.googleapis.com/css2?family=Mulish:ital,wght@0,400;0,600;0,700;0,800;1,400&display=swap" rel="stylesheet">
<style>
:root{
  --wine:#8b1c24;
  --wine-dark:#6e141b;
  --orange:#f0901a;
  --ink:#333333;
  --muted:#666666;
  --line:#dddddd;
  --paper:#ffffff;
  --mist:#f6f6f6;
  --night:#2b2a2b;
  --review-green:#34b182;
  --feed-blue:#3b5998;
}
*{box-sizing:border-box;margin:0;padding:0}
html,body{width:1200px;height:2353px;overflow:hidden}
body{font-family:"Mulish",Arial,sans-serif;color:var(--ink);background:var(--paper);position:relative}
.abs{position:absolute}

/* header */
.site-header{position:absolute;left:0;top:0;width:1200px;height:129px;background:var(--paper)}
.brand{position:absolute;left:140px;top:0;width:182px;height:160px;background:var(--paper);z-index:3;border-radius:0 0 6px 6px;display:flex;flex-direction:column;align-items:center;justify-content:center;gap:4px}
.brand-name{font-size:30px;font-weight:700;color:var(--wine);letter-spacing:1px}
.brand-sub{font-size:10px;font-weight:700;color:var(--wine);letter-spacing:1px;text-transform:uppercase}
.info{position:absolute;top:22px;display:flex;gap:10px;font-size:11px;line-height:18px;color:var(--muted)}
.info .accent{color:var(--wine)}
.info svg{flex:none;margin-top:2px}
.main-nav{position:absolute;left:520px;top:84px;display:flex;gap:0}
.main-nav a{font-size:13px;color:var(--ink);text-decoration:none;text-transform:uppercase;width:120px;text-align:center}
.main-nav a:nth-child(2){width:90px}
.main-nav a.active{color:var(--orange)}
.search{position:absolute;left:883px;top:82px;width:185px;height:27px;border:1px solid var(--line);border-radius:14px;font-size:10px;color:#aaa;padding:7px 12px}
.search svg{position:absolute;right:10px;top:8px}

/* hero */
.hero{position:absolute;left:0;top:129px;width:1200px;height:621px;background:linear-gradient(180deg,#3a2a22 0%,#54412f 40%,#2f2420 100%)}
.hero-title{position:absolute;left:0;width:1200px;text-align:center;color:#fff}
.hero-kicker{top:165px;font-size:28px;font-weight:600;letter-spacing:1px}
.hero-head{top:205px;font-size:56px;font-weight:800}
.btn{display:inline-block;background:var(--orange);color:#fff;border-radius:22px;font-weight:700;text-transform:uppercase;text-align:center}
.hero .btn{position:absolute;left:516px;top:290px;width:168px;height:41px;line-height:41px;font-size:12px}
.hero-arrows{position:absolute;left:572px;top:389px;display:flex;gap:12px}

/* band */
.wine-band{position:absolute;left:0;top:750px;width:1200px;height:753px;background:var(--wine)}

/* reservation */
.reservation{position:absolute;left:132px;top:571px;width:936px;z-index:2}
.reservation-tab{width:179px;height:50px;background:var(--orange);color:#fff;font-size:18px;font-weight:700;line-height:50px;text-align:center}
.reservation-form{background:#fff;height:289px;position:relative;box-shadow:0 2px 6px rgba(0,0,0,.25)}
.field{position:absolute;height:40px;border:1px solid var(--line);font-size:11px;color:#999;padding:12px 10px}
.field svg{position:absolute;right:9px;top:13px}
.field.comments{height:79px}
.reservation .btn{position:absolute;left:811px;top:229px;width:103px;height:39px;line-height:39px;font-size:12px;border-radius:20px}

/* tours */
.section-title{position:absolute;left:0;width:1200px;text-align:center;font-weight:400}
.tours-title{top:962px;font-size:28px;color:#fff}
.tours-intro{top:1005px;font-size:12px;line-height:22px;color:#fff}
.tour-card{position:absolute;top:1075px;width:292px;height:359px;border:1px solid #e5b5b8;text-align:center;color:#fff}
.tour-photo{height:179px;background:linear-gradient(135deg,#c7a35a 0%,#7b8a3e 55%,#3f5a2a 100%)}
.tour-card h3{font-size:14px;font-weight:400;margin-top:16px}
.tour-card p{font-size:11px;line-height:22px;margin:8px 22px 0}
.tour-card .btn{width:102px;height:36px;line-height:36px;font-size:11px;margin-top:14px;text-transform:none;font-weight:400;border-radius:18px}

/* blog */
.blog-title{position:absolute;left:132px;top:1553px;font-size:20px;font-weight:400}
.blog-nav{position:absolute;left:698px;top:1560px;font-size:12px;color:#aaa}
.post{position:absolute;left:132px;width:586px;height:132px}
.post-photo{position:absolute;left:0;top:0;width:152px;height:132px;border-radius:4px;background:linear-gradient(135deg,#4a1a15 0%,#8a3a22 50%,#c58a4a 100%)}
.post-body{position:absolute;left:182px;top:0;right:0}
.post-body h4{font-size:14px;font-weight:400;color:#444}
.post-date{font-size:11px;color:var(--orange);margin-top:10px}
.post-body p{font-size:11px;line-height:22px;color:var(--muted);margin-top:6px}
.read-more{font-size:11px;color:var(--orange);margin-top:6px}
.post-divider{position:absolute;left:132px;top:1749px;width:586px;border-top:1px solid var(--line)}

.feed{position:absolute;left:778px;top:1559px;width:290px;height:336px;border:1px solid var(--line)}
.feed-title{position:absolute;left:14px;top:14px;font-size:22px;font-weight:700;color:var(--feed-blue);display:flex;align-items:center;gap:8px}
.feed-title i{display:block;width:20px;height:20px;background:var(--feed-blue)}
.feed-brand{position:absolute;left:16px;top:60px;font-size:13px;font-weight:700;color:var(--wine)}
.feed-like{position:absolute;left:182px;top:64px;width:71px;height:30px;border:1px solid #9aa9c8;border-radius:3px;background:#eef1f7;font-size:13px;color:var(--feed-blue);text-align:center;line-height:28px}
.feed-item{position:absolute;left:16px;width:256px;border-top:1px solid var(--line);padding-top:8px}
.feed-avatar{position:absolute;left:0;top:8px;width:50px;height:52px;background:linear-gradient(135deg,#6b6f78,#2f3238)}
.feed-text{margin-left:66px;font-size:9px;line-height:13px;color:#555}
.feed-text b{color:var(--feed-blue);font-weight:700}
.feed-text .act{color:var(--feed-blue)}
.feed-share{position:absolute;left:18px;top:298px;width:62px;height:20px;background:var(--feed-blue);border-radius:2px;font-size:8px;color:#fff;text-align:center;line-height:20px}

/* reviews */
.reviews{position:absolute;left:0;top:1955px;width:1200px;height:310px;background:var(--mist);border-top:1px solid #e4e4e4}
.reviews-title{top:55px;font-size:20px}
.review{position:absolute;top:94px;width:284px}
.review-mark{font-size:24px;color:#aaa;font-style:italic;line-height:14px}
.review p{font-size:11px;line-height:22px;font-style:italic;color:var(--muted);margin-top:2px}
.review-avatar{position:absolute;left:0;top:120px;width:60px;height:60px;border-radius:50%;background:linear-gradient(135deg,#d8c2aa,#8a6d55)}
.review-brand{position:absolute;left:74px;top:122px;display:flex;align-items:center;gap:6px;font-size:16px;font-weight:700;color:#222}
.review-brand i{display:block;width:12px;height:12px;border-radius:50%;background:#222}
.stars{position:absolute;left:74px;top:150px;display:flex;gap:3px}
.stars span{width:19px;height:19px;background:var(--review-green);display:block}

/* footer */
.site-footer{position:absolute;left:0;top:2265px;width:1200px;height:88px;background:var(--night);color:#fff}
.footer-nav{position:absolute;left:132px;top:28px;font-size:10px;letter-spacing:.3px}
.copyright{position:absolute;left:132px;top:52px;font-size:10px;letter-spacing:.3px}
.connect{position:absolute;left:843px;top:35px;font-size:10px;display:flex;align-items:center;gap:10px}
.connect i{display:block;width:27px;height:27px;border-radius:50%}
</style>
</head>
<body>

<header class="site-header">
  <div class="brand">
    <div class="brand-name">VINORA</div>
    <div class="brand-sub">Italian Cuisine &amp; Wine Bar</div>
  </div>
  <div class="info" style="left:697px">
    <svg width="22" height="22" viewBox="0 0 22 22"><circle cx="11" cy="11" r="9" fill="none" stroke="#8b1c24" stroke-width="2"/><path d="M11 6v5l3 3" fill="none" stroke="#8b1c24" stroke-width="2"/></svg>
    <div>Open Daily From<br><span class="accent">5 to 12 am</span></div>
  </div>
  <div class="info" style="left:843px">
    <svg width="18" height="24" viewBox="0 0 18 24"><path d="M9 1C4.6 1 1 4.5 1 8.8 1 14.5 9 23 9 23s8-8.5 8-14.2C17 4.5 13.4 1 9 1z" fill="#8b1c24"/><circle cx="9" cy="9" r="3" fill="#fff"/></svg>
    <div>Tel. 555 0148 Calle Olivo s/n L-3. Centro<br>Puerto Alma, Mexico</div>
  </div>
  <nav class="main-nav">
    <a class="active">Home</a><a>Menu</a><a>Reservations</a>
  </nav>
  <div class="search">Search
    <svg width="10" height="10" viewBox="0 0 10 10"><circle cx="4" cy="4" r="3" fill="none" stroke="#999" stroke-width="1.3"/><path d="M6.3 6.3L9 9" stroke="#999" stroke-width="1.3"/></svg>
  </div>
</header>

<section class="hero" role="img" aria-label="Busy bistro interior with guests dining and a bar in the background">
  <div class="hero-title hero-kicker">HIGH QUALITY</div>
  <div class="hero-title hero-head">FOOD AND WINES</div>
  <span class="btn">Learn More Info</span>
  <div class="hero-arrows">
    <svg width="22" height="22" viewBox="0 0 22 22"><circle cx="11" cy="11" r="9" fill="none" stroke="#fff" stroke-width="2"/><path d="M13 7l-4 4 4 4" fill="none" stroke="#fff" stroke-width="2"/></svg>
    <svg width="22" height="22" viewBox="0 0 22 22"><circle cx="11" cy="11" r="9" fill="none" stroke="#fff" stroke-width="2"/><path d="M9 7l4 4-4 4" fill="none" stroke="#fff" stroke-width="2"/></svg>
  </div>
</section>

<div class="wine-band"></div>

<section class="reservation">
  <div class="reservation-tab">RESERVATION</div>
  <div class="reservation-form">
    <div class="field" style="left:18px;top:25px;width:108px">Date<svg width="10" height="10"><rect x="1" y="2" width="8" height="7" fill="none" stroke="#999"/></svg></div>
    <div class="field" style="left:130px;top:25px;width:106px">Time<svg width="10" height="10"><circle cx="5" cy="5" r="4" fill="none" stroke="#999"/></svg></div>
    <div class="field" style="left:243px;top:25px;width:218px">Party Size<svg width="10" height="10"><path d="M5 1v8M2 6c0 2 6 2 6 0" fill="none" stroke="#999"/></svg></div>
    <div class="field" style="left:469px;top:25px;width:218px">Name<svg width="10" height="10"><circle cx="5" cy="5" r="4" fill="none" stroke="#999"/></svg></div>
    <div class="field" style="left:696px;top:25px;width:218px">Email<svg width="10" height="10"><rect x="1" y="2" width="8" height="6" fill="#999"/></svg></div>
    <div class="field" style="left:18px;top:82px;width:218px">Phone Number (Optional)<svg width="10" height="10"><path d="M2 1l2 2-1 2 2 2 2-1 2 2-2 2C4 9 1 6 1 2z" fill="#999"/></svg></div>
    <div class="field" style="left:243px;top:82px;width:218px">Hotel Name<svg width="10" height="10"><rect x="2" y="1" width="6" height="8" fill="none" stroke="#999"/></svg></div>
    <div class="field" style="left:469px;top:82px;width:218px">Room Number<svg width="10" height="10"><path d="M1 8V3M1 6h8v2" fill="none" stroke="#999"/></svg></div>
    <div class="field" style="left:696px;top:82px;width:218px">Guest Email<svg width="10" height="10"><circle cx="5" cy="3" r="2" fill="#999"/><rect x="2" y="6" width="6" height="3" fill="#999"/></svg></div>
    <div class="field comments" style="left:18px;top:138px;width:896px">Comments (Optional)<svg width="10" height="10"><ellipse cx="5" cy="4" rx="4" ry="3" fill="#999"/></svg></div>
    <span class="btn">Send</span>
  </div>
</section>

<h2 class="section-title tours-title">Wine Tasting &amp; Wine Pairing Tours</h2>
<p class="section-title tours-intro">To gather those who have impacted our lives and supported us in this wonderful town, bring them high quality food and<br>wines, while simultaneously offering affordable prices to locals and visitors.</p>

<article class="tour-card" style="left:132px">
  <div class="tour-photo" role="img" aria-label="Friends toasting with wine outdoors at sunset"></div>
  <h3>Ratione Voluptatem</h3>
  <p>Beatae vitae dicta sunt explicaboes ipsam voluptatem quia voluptas sit aspernatur sed consequuntur...</p>
  <span class="btn">Learn More</span>
</article>
<article class="tour-card" style="left:455px">
  <div class="tour-photo" role="img" aria-label="Guest laughing with a glass of white wine in a vineyard"></div>
  <h3>Ratione Voluptatem</h3>
  <p>Beatae vitae dicta sunt explicaboes ipsam voluptatem quia voluptas sit aspernatur sed consequuntur...</p>
  <span class="btn">Learn More</span>
</article>
<article class="tour-card" style="left:776px">
  <div class="tour-photo" role="img" aria-label="Group sharing wine at an outdoor picnic table"></div>
  <h3>Ratione Voluptatem</h3>
  <p>Beatae vitae dicta sunt explicaboes ipsam voluptatem quia voluptas sit aspernatur sed consequuntur...</p>
  <span class="btn">Learn More</span>
</article>

<h2 class="blog-title">Latest Blog</h2>
<div class="blog-nav">&lsaquo; &rsaquo;</div>

<article class="post" style="top:1603px">
  <div class="post-photo" role="img" aria-label="Glasses of red wine beside a wooden barrel"></div>
  <div class="post-body">
    <h4>Excepteur sint occaecat cupidatat non proident</h4>
    <div class="post-date">&#9638; Posted on 23 june,2017</div>
    <p>Adipiscing elit, sed do eiusmod tempor incididunt ut labore et dolore magna aliqua. Ut enim ad minim veniam, quis nostrud exercitation...</p>
    <div class="read-more">Read More</div>
  </div>
</article>
<div class="post-divider"></div>
<article class="post" style="top:1763px">
  <div class="post-photo" role="img" aria-label="Raised wine glasses in a toast under warm lights"></div>
  <div class="post-body">
    <h4>Excepteur sint occaecat cupidatat non proident</h4>
    <div class="post-date">&#9638; Posted on 23 june,2017</div>
    <p>Adipiscing elit, sed do eiusmod tempor incididunt ut labore et dolore magna aliqua. Ut enim ad minim veniam, quis nostrud exercitation...</p>
    <div class="read-more">Read More</div>
  </div>
</article>

<aside class="feed">
  <div class="feed-title"><i></i>CHATTERLY FEED</div>
  <div class="feed-brand">VINORA BISTRO</div>
  <div class="feed-like">Like</div>
  <div class="feed-item" style="top:124px">
    <div class="feed-avatar" role="img" aria-label="Profile photo"></div>
    <div class="feed-text"><b>Dario Fenwick</b><br>Fusce eu lorem dui. Integer eu venen atis lectus sed blandit urna<br><span class="act">Like :: Comment</span></div>
  </div>
  <div class="feed-item" style="top:203px">
    <div class="feed-avatar" role="img" aria-label="Profile photo"></div>
    <div class="feed-text"><b>Dario Fenwick</b><br>Fusce eu lorem dui. Integer eu venen atis lectus sed blandit urna<br><span class="act">Like :: Comment</span></div>
  </div>
  <div class="feed-share">SHARE</div>
</aside>

<section class="reviews">
  <h2 class="section-title reviews-title">Last Review</h2>
  <div class="review" style="left:132px">
    <div class="review-mark">&ldquo;</div>
    <p>Aliquip ex ea commodo consequat. Duis aute irure dolo in reprehenderit in voluptate velit esse cillum dolore eu fugiat nulla pariatur...</p>
    <div class="review-avatar" role="img" aria-label="Reviewer portrait"></div>
    <div class="review-brand"><i></i>Wandermeter</div>
    <div class="stars"><span></span><span></span><span></span><span></span><span></span></div>
  </div>
  <div class="review" style="left:458px">
    <div class="review-mark">&ldquo;</div>
    <p>Aliquip ex ea commodo consequat. Duis aute irure dolo in reprehenderit in voluptate velit esse cillum dolore eu fugiat nulla pariatur...</p>
    <div class="review-avatar" role="img" aria-label="Reviewer portrait"></div>
    <div class="review-brand"><i></i>Wandermeter</div>
    <div class="stars"><span></span><span></span><span></span><span></span><span></span></div>
  </div>
  <div class="review" style="left:784px">
    <div class="review-mark">&ldquo;</div>
    <p>Aliquip ex ea commodo consequat. Duis aute irure dolo in reprehenderit in voluptate velit esse cillum dolore eu fugiat nulla pariatur...</p>
    <div class="review-avatar" role="img" aria-label="Reviewer portrait"></div>
    <div class="review-brand"><i></i>Wandermeter</div>
    <div class="stars"><span></span><span></span><span></span><span></span><span></span></div>
  </div>
</section>

<footer class="site-footer">
  <div class="footer-nav">HOME &nbsp;|&nbsp; MENU &nbsp;|&nbsp; RESERVATIONS &nbsp;|&nbsp; CONTACT US</div>
  <div class="copyright">COPYRIGHTS © 2017 , VINORABISTRO | ALL RIGHTS RESERVED.</div>
  <div class="connect">CONNECT WITH US :
    <i style="background:#3b5998" aria-label="Chatterly"></i>
    <i style="background:#1da1f2" aria-label="Chirper"></i>
    <i style="background:#d9302c" aria-label="Vidstream"></i>
    <i style="background:#a88a5a" aria-label="Snapgram"></i>
  </div>
</footer>

</body>
</html>
```